B2B Energy Broker Website

Our current website looks amateur, we need something far more professional looking and advanced. Current website is www.halvorn-utilitypartners.com

```html
<!DOCTYPE html>
<html lang="en">
<head>
<meta charset="utf-8">
<title>Halvorn Utility Partners</title>
<link rel="stylesheet" href="https://fonts.googleapis.com/css2?family=Poppins:wght@300;400;500;600;700&display=swap">
<style>
:root{
  --charcoal:#4a4a4a;
  --charcoal-dark:#3a3a3a;
  --ink:#444;
  --muted:#777;
  --light:#efefef;
  --white:#fff;
  --line:#e2e2e2;
}
*{box-sizing:border-box;margin:0;padding:0}
html,body{width:1200px;height:3679px;overflow:hidden}
body{font-family:'Poppins',sans-serif;color:var(--ink);background:var(--white);position:relative}
.abs{position:absolute}

/* header */
.brand{left:121px;top:14px;display:flex;align-items:center;gap:10px}
.brand-dot{width:48px;height:48px;border-radius:50%;background:var(--charcoal)}
.brand-name{font-size:22px;font-weight:400;letter-spacing:3px;color:var(--charcoal);line-height:1.1}
.nav{top:30px;left:0;width:1200px;height:20px}
.nav a{position:absolute;font-size:11.5px;color:var(--ink);text-decoration:none}

/* hero */
.hero{left:0;top:0;width:1200px;height:600px;background:linear-gradient(90deg,#fbfbfb 0%,#f1f1f1 45%,#e6e6e6 100%)}
.hero-photo{left:514px;top:0;width:686px;height:600px;background:radial-gradient(ellipse at 55% 40%,#d8c7b8 0%,#e4e0dc 35%,#eceae8 70%,#e2e3e4 100%)}
.hero-title{left:121px;top:210px;font-size:45px;font-weight:700;line-height:48px;color:var(--charcoal);letter-spacing:1px}
.hero-sub{left:121px;top:366px;font-size:14px;color:var(--ink)}
.btn-dark{background:var(--charcoal);color:var(--white);font-size:11.5px;font-weight:500;display:flex;align-items:center;justify-content:center;border-radius:3px}
.hero-btn{left:121px;top:419px;width:168px;height:35px}

/* welcome */
.welcome{left:0;top:600px;width:1200px;height:540px;background:var(--charcoal)}
.welcome-glow{left:70px;top:690px;width:220px;height:360px;background:radial-gradient(ellipse,#6a6a6a 0%,rgba(74,74,74,0) 70%)}
.welcome-photo{left:190px;top:692px;width:358px;height:358px;border-radius:50%;background:radial-gradient(circle at 45% 40%,#a7adb4 0%,#8f99a5 45%,#6d7885 100%)}
.welcome-badge{left:440px;top:942px;width:108px;height:108px;border-radius:50%;background:var(--charcoal)}
.welcome-kicker{left:610px;top:668px;font-size:37px;font-weight:300;color:var(--white)}
.welcome-title{left:610px;top:710px;font-size:35px;font-weight:600;line-height:42px;color:var(--white)}
.welcome-text{left:610px;top:806px;width:375px;font-size:12px;line-height:21.6px;color:#f2f2f2}
.btn-light{left:610px;top:1006px;width:149px;height:35px;background:var(--white);color:var(--charcoal);font-size:11.5px;font-weight:500;display:flex;align-items:center;justify-content:center;border-radius:3px}

/* services */
.services{left:0;top:1140px;width:1200px;height:679px;background:var(--light)}
.service-card{width:340px;height:269px;background:var(--charcoal);border-radius:7px;color:var(--white);text-align:center;padding-top:48px}
.service-card svg{display:block;margin:0 auto}
.service-card h3{font-size:21px;font-weight:600;margin-top:10px;letter-spacing:.3px}
.service-card p{font-size:11px;line-height:18px;color:#e8e8e8;width:250px;margin:6px auto 0}

/* suppliers */
.suppliers{left:0;top:1819px;width:1200px;height:203px;background:var(--white)}
.supplier{top:1908px;width:160px;text-align:center;font-size:17px;font-weight:500;color:var(--charcoal)}

/* help */
.help{left:0;top:2022px;width:1200px;height:270px;background:var(--charcoal)}
.help-photo{left:650px;top:1960px;width:336px;height:332px;background:linear-gradient(180deg,#c6a488 0%,#e9e9e9 30%,#d6d6d6 70%,#8f8f8f 100%);border-radius:150px 150px 0 0}
.help-title{left:250px;top:2092px;font-size:37px;font-weight:600;color:var(--white)}
.help-line{left:250px;font-size:22px;font-weight:300;color:var(--white)}
.help-line strong{font-weight:600}

/* features */
.features{left:0;top:2292px;width:1200px;height:325px;background:var(--white)}
.feature{top:2352px;width:200px;text-align:center}
.feature svg{display:block;margin:0 auto}
.feature h4{font-size:18.5px;font-weight:500;line-height:24px;color:var(--ink);margin-top:8px}
.feature p{font-size:11px;line-height:18px;color:var(--muted);margin-top:8px}

/* faq */
.faq{left:0;top:2617px;width:1200px;height:733px;background:var(--light)}
.faq-title{left:0;top:2664px;width:1200px;text-align:center;font-size:36px;font-weight:600;color:var(--charcoal);letter-spacing:.5px}
.faq-item{left:250px;width:700px;height:34px;background:var(--white);border-radius:3px;display:flex;align-items:center;justify-content:space-between;padding:0 22px 0 24px;font-size:12px;color:var(--ink)}
.faq-item span.sign{font-size:22px;font-weight:300;color:var(--ink)}
.faq-answer{left:274px;top:2988px;width:640px;font-size:11px;line-height:18px;color:var(--muted)}
.faq-answer p{margin-bottom:18px}
.faq-btn{left:526px;top:3284px;width:108px;height:35px}

/* footer */
.footer{left:0;top:3350px;width:1200px;height:329px;background:var(--charcoal)}
.footer-curve{left:0;top:3328px;width:380px;height:351px}
.footer-brand{left:502px;top:3388px;display:flex;align-items:center;gap:8px;color:var(--white)}
.footer-brand .brand-dot{width:46px;height:46px;background:var(--white)}
.footer-brand .brand-name{color:var(--white)}
.footer-col{top:3475px;color:var(--white)}
.footer-col h5{font-size:12px;font-weight:500;margin-bottom:6px}
.footer-col li{list-style:none;font-size:9.5px;line-height:18px;display:flex;align-items:flex-start;gap:6px}
.footer-col li::before{content:"";width:5px;height:5px;border-radius:50%;background:var(--white);margin-top:7px;flex:none}
.footer-col.contacts li::before{display:none}
.footer-col.contacts li{margin-bottom:12px;line-height:14px}
.footer-rule{left:439px;top:3628px;width:512px;height:1px;background:#6a6a6a}
.footer-small{top:3646px;font-size:9px;color:var(--white)}
</style>
</head>
<body>

<!-- hero -->
<div class="abs hero"></div>
<div class="abs hero-photo" role="img" aria-label="Smiling businesswoman holding a tablet in a bright office"></div>
<div class="abs brand"><div class="brand-dot"></div><div class="brand-name">HALVORN<br><span style="font-size:12.5px;letter-spacing:.3px">utility partners</span></div></div>
<nav class="abs nav">
  <a style="left:766px">Home</a>
  <a style="left:831px">About Us</a>
  <a style="left:913px">Services</a>
  <a style="left:990px">FAQs</a>
  <a style="left:1051px">Contact Us</a>
</nav>
<h1 class="abs hero-title">TRANSPARENT<br>ENERGY<br>SAVINGS</h1>
<div class="abs hero-sub">Unbiased For Your Business</div>
<div class="abs btn-dark hero-btn">GET STARTED</div>

<!-- welcome -->
<div class="abs welcome"></div>
<div class="abs welcome-glow" role="img" aria-label="Faint light bulb in the shadows"></div>
<div class="abs welcome-photo" role="img" aria-label="Two businessmen shaking hands in an office"></div>
<div class="abs welcome-badge"></div>
<div class="abs welcome-kicker">Welcome To</div>
<h2 class="abs welcome-title">HALVORN UTILITY<br>PARTNERS</h2>
<p class="abs welcome-text">Along with providing competitive business energy procurement, we run a complete service solution for your ongoing energy requirements. We can take total management of your bills, supplier relationship, renewals and more. If you are concerned about a more complex arrangement for your energy supply then we will endeavour to take over the time spent on it and allow you as much or as little involvement as you desire.</p>
<div class="abs btn-light">ABOUT US</div>

<!-- services -->
<div class="abs services"></div>
<div class="abs service-card" style="left:250px;top:1200px">
  <svg width="46" height="60" viewBox="0 0 46 60"><path d="M23 2c4 12 20 20 20 36a20 20 0 0 1-40 0c0-9 5-15 9-19 0 7 3 11 6 12-2-10 1-21 5-29z" fill="#fff"/><path d="M23 36c3 4 7 7 7 12a7 7 0 0 1-14 0c0-5 4-8 7-12z" fill="#4a4a4a"/></svg>
  <h3>COMMERCIAL GAS</h3>
  <p>We offer an impartial review of your business gas requirements to ensure you are getting the best prices, service and management as a total package.</p>
</div>
<div class="abs service-card" style="left:610px;top:1200px">
  <svg width="60" height="60" viewBox="0 0 60 60"><g transform="rotate(45 30 30)" fill="#fff"><rect x="22" y="2" width="4" height="14" rx="2"/><rect x="34" y="2" width="4" height="14" rx="2"/><path d="M16 16h28v10a14 14 0 0 1-28 0z"/><rect x="27" y="38" width="6" height="20" rx="2"/></g></svg>
  <h3>COMMERCIAL ELECTRICITY</h3>
  <p>We offer an impartial review of your business electricity requirements to ensure you are getting the best price, service and management as a total package.</p>
</div>
<div class="abs service-card" style="left:250px;top:1489px">
  <svg width="58" height="60" viewBox="0 0 58 60"><g fill="#fff"><circle cx="29" cy="30" r="20"/><g><rect x="25" y="2" width="8" height="12" rx="2"/><rect x="25" y="46" width="8" height="12" rx="2"/><rect x="1" y="26" width="12" height="8" rx="2"/><rect x="45" y="26" width="12" height="8" rx="2"/></g><g transform="rotate(45 29 30)"><rect x="25" y="2" width="8" height="12" rx="2"/><rect x="25" y="46" width="8" height="12" rx="2"/><rect x="1" y="26" width="12" height="8" rx="2"/><rect x="45" y="26" width="12" height="8" rx="2"/></g></g><circle cx="29" cy="30" r="11" fill="#4a4a4a"/><rect x="26" y="22" width="6" height="20" rx="3" fill="#fff"/></svg>
  <h3>UTILITY SERVICES</h3>
  <p>We can provide a wide range of business utility management services to ensure your time and money is better spent.</p>
</div>
<div class="abs service-card" style="left:610px;top:1489px">
  <svg width="40" height="60" viewBox="0 0 40 60"><path d="M20 4C26 18 38 30 38 41a18 18 0 0 1-36 0C2 30 14 18 20 4z" fill="#fff"/></svg>
  <h3>COMMERCIAL WATER</h3>
  <p>The commercial water market has now been de-regulated. Speak to our team to find out how we can save you money on your water and waste bills.</p>
</div>

<!-- suppliers -->
<div class="abs suppliers"></div>
<div class="abs supplier" style="left:104px">Northvale Power</div>
<div class="abs supplier" style="left:270px">Brightwell Energy</div>
<div class="abs supplier" style="left:440px">Ardent Energy</div>
<div class="abs supplier" style="left:606px">Kestrel Energy</div>
<div class="abs supplier" style="left:766px">Albion Gas</div>
<div class="abs supplier" style="left:930px">Harbourline Power</div>

<!-- help -->
<div class="abs help"></div>
<div class="abs help-photo" role="img" aria-label="Support agent with headset, arms crossed"></div>
<h2 class="abs help-title">How can we help?</h2>
<div class="abs help-line" style="top:2148px">Contact Halvorn Utility Now</div>
<div class="abs help-line" style="top:2178px">On <strong>0300 555 0142</strong> To Start Saving</div>

<!-- features -->
<div class="abs features"></div>
<div class="abs feature" style="left:256px">
  <svg width="44" height="44" viewBox="0 0 44 44"><circle cx="24" cy="18" r="14" fill="none" stroke="#4a4a4a" stroke-width="4"/><rect x="18" y="18" width="3" height="7" fill="#4a4a4a"/><rect x="23" y="12" width="3" height="13" fill="#4a4a4a"/><rect x="28" y="15" width="3" height="10" fill="#4a4a4a"/><path d="M14 28 4 40" stroke="#4a4a4a" stroke-width="6" stroke-linecap="round"/></svg>
  <h4>Market Trend<br>Analysis</h4>
  <p>Our energy analysts monitor a live energy market curve to ensure you buy at the right time and save as much as possible.</p>
</div>
<div class="abs feature" style="left:500px">
  <svg width="48" height="44" viewBox="0 0 48 44"><g fill="#4a4a4a"><circle cx="24" cy="6" r="5"/><path d="M17 20a7 7 0 0 1 14 0z"/><circle cx="10" cy="26" r="4.5"/><path d="M3 40a7 7 0 0 1 14 0z"/><circle cx="24" cy="26" r="4.5"/><path d="M17 40a7 7 0 0 1 14 0z"/><circle cx="38" cy="26" r="4.5"/><path d="M31 40a7 7 0 0 1 14 0z"/><rect x="9" y="21" width="30" height="2"/></g></svg>
  <h4>Direct<br>Relationships</h4>
  <p>We hold direct relationships with over 18 major suppliers, we use these relationships to ensure you get the most from your supplier.</p>
</div>
<div class="abs feature" style="left:746px">
  <svg width="44" height="44" viewBox="0 0 44 44"><path d="M22 3a16 16 0 0 1 16 16c0 6-4 9-6 12v10H16v-6h-6v-9l-4-3 4-4c0-9 5-16 12-16z" fill="#4a4a4a"/></svg>
  <h4>Industry<br>Experience</h4>
  <p>Our two founders hold over 30 years industry experience between them and our staff are what we believe to be the best in the industry.</p>
</div>

<!-- faq -->
<div class="abs faq"></div>
<h2 class="abs faq-title">FREQUENTLY ASKED QUESTIONS</h2>
<div class="abs faq-item" style="top:2751px">Why Should My Business Use Halvorn Utility Partners?<span class="sign">+</span></div>
<div class="abs faq-item" style="top:2799px">Who Should Consider Using Halvorn Utility Partners?<span class="sign">+</span></div>
<div class="abs faq-item" style="top:2847px">Is Halvorn Utility Partners Independent?<span class="sign">+</span></div>
<div class="abs faq-item" style="top:2895px">Will There Be A Charge For Gaining Quotations?<span class="sign">+</span></div>
<div class="abs faq-item" style="top:2943px">How Do You Achieve Better Prices Than If I Go Direct?<span class="sign">&minus;</span></div>
<div class="abs faq-answer">
  <p>We have worked hard to build close relationships with all our energy supplier partners.</p>
  <p>We also have many ways in which we can procure your future energy. Such as group bulk purchase, single entity, fixed, flex..... the options are many.</p>
  <p>As a successful energy consultancy we deliver our energy suppliers with regular business. This also provides us with some of the most competitive pricing within the third party intermediaries arena. Therefore we always achieve and importantly present the best price from one of many UK energy suppliers.</p>
  <p>Caution : to efficiently scan the complete market takes both time and serious effort.</p>
  <p>Whilst most businesses are more switched on to energy pit falls &ndash; sadly most business still do not have time allocated or resources to trawl and engage with all different energy suppliers.</p>
  <p>Proudly at Halvorn Utility Partners we are simply a one point of contact for everything business energy.</p>
</div>
<div class="abs btn-dark faq-btn">VIEW MORE</div>

<!-- footer -->
<div class="abs footer"></div>
<svg class="abs footer-curve" viewBox="0 0 380 351"><path d="M0 0h170c120 0 200 90 210 351H0z" fill="#3a3a3a"/></svg>
<div class="abs footer-brand"><div class="brand-dot"></div><div class="brand-name">HALVORN<br><span style="font-size:12.5px;letter-spacing:.3px">utility partners</span></div></div>
<div class="abs footer-col" style="left:439px">
  <h5>Quick Links</h5>
  <ul><li>Home</li><li>About Us</li><li>Services</li><li>FAQs</li><li>Contact Us</li></ul>
</div>
<div class="abs footer-col" style="left:603px">
  <h5>Links</h5>
  <ul><li>Privacy Policy</li><li>Cookie Policy</li><li>Terms &amp; Conditions</li></ul>
</div>
<div class="abs footer-col contacts" style="left:799px">
  <h5>Contacts</h5>
  <ul>
    <li><svg width="10" height="12" viewBox="0 0 10 12"><path d="M5 0a4 4 0 0 1 4 4c0 3-4 8-4 8S1 7 1 4a4 4 0 0 1 4-4z" fill="#fff"/><circle cx="5" cy="4" r="1.5" fill="#4a4a4a"/></svg><span>Unit 7 Marlow Court<br>Ashford, AB1 2CD</span></li>
    <li><svg width="10" height="12" viewBox="0 0 10 12"><path d="M2 1l2 3-1 1c1 2 2 3 4 4l1-1 2 2-1 2C4 11 0 7 0 3z" fill="#fff"/></svg><span>Phone: 0300 555 0142<br>Fax: 0300 555 0143</span></li>
    <li><svg width="10" height="12" viewBox="0 0 10 12"><rect x="0" y="3" width="10" height="7" rx="1" fill="#fff"/><path d="M0 4l5 3 5-3" stroke="#4a4a4a" fill="none"/></svg><span>info@halvorn-utilitypartners.com</span></li>
  </ul>
</div>
<div class="abs footer-rule"></div>
<div class="abs footer-small" style="left:439px">&copy; 2022 Halvorn Utility Partners. All Rights Reserved</div>
<div class="abs footer-small" style="left:796px">Web Design UK By Fernlake Studio</div>

</body>
</html>
```